Flyer for annual KESTREL SUMMIT 2020

I would like a church event flyer designed. The event is called "KESTREL SUMMIT 2020". I am looking for a professional, yet catchy design that uses our brand colors and logo creatively while communicating key information of the event effectively.

1. The logo is attached in two color formats. The designer has the choice to use them as he/she want.

2. The location of the event is: Harlow Community Center, 239 Fennimore Street, Portland, ME 04117

3. Time and date of event. The designer can organize and format the date and time as he/she pleases.
Thursday December 31st @ 6:30PM
Friday January 1st @ 6:30PM
Saturday 2nd @ 6:30PM
Sunday 3rd @ 4:30PM

4. The topic of the event is "In Fire and On Fire". The designer is free to use this phrase as he/she pleases to create a good composition.

5. Speaker: Prophet Marcus Olunde (2 pictures of the speaker to choose from are attached)

6. Contact information: contact@brightmeadowfold.org - Telephone number: 207 583 2914

7. I would also like the following three words on the flyer. These words describe the focus of the event: FIRE, REVIVAL, PROPHETIC

Target Market(s)

Young adults

Font styles to use
Sans Serif

Requirements
Must have
• Logo, speaker's picture
Should not have
• cross image, church image

```html
<!DOCTYPE html>
<html lang="en">
<head>
<meta charset="utf-8">
<title>Kestrel Summit 2020 Flyer</title>
<link rel="stylesheet" href="https://fonts.googleapis.com/css2?family=Playfair+Display:wght@400;700&family=Great+Vibes&family=Libre+Baskerville&family=Open+Sans:wght@400;700&display=swap">
<style>
  :root {
    --flame-light: #f6a52c;
    --flame-mid: #ec6f2a;
    --ember-red: #c62334;
    --deep-red: #b81e34;
    --title-red: #ec1840;
    --band-orange: #ee8426;
    --ink-white: #ffffff;
    --speaker-orange: #f39a2a;
  }
  * { margin: 0; padding: 0; box-sizing: border-box; }
  html, body { width: 1200px; height: 1200px; overflow: hidden; background: #ffffff; }
  .flyer {
    position: absolute; left: 153px; top: 20px; width: 894px; height: 1160px; overflow: hidden;
    background: linear-gradient(180deg, var(--flame-light) 0%, var(--flame-mid) 40%, #e2472d 75%, var(--ember-red) 100%);
    color: var(--ink-white);
  }
  .flyer > * { position: absolute; }
  .year {
    left: 118px; top: 211px; transform: rotate(-90deg); transform-origin: left top;
    font: 400 54px/1 "Open Sans", sans-serif; letter-spacing: 2px; color: var(--ink-white);
  }
  .event-name {
    left: 176px; top: 58px; font: 400 104px/1 "Playfair Display", serif; color: var(--title-red); letter-spacing: 1px;
  }
  .event-kind {
    left: 230px; top: 150px; font: 400 110px/1 "Great Vibes", cursive; color: var(--ink-white);
  }
  .title-rule { height: 2px; background: var(--title-red); top: 224px; }
  .title-rule.left { left: 89px; width: 270px; }
  .title-rule.right { left: 420px; width: 427px; }
  .theme-band { left: 0; top: 301px; width: 894px; height: 76px; background: rgba(238,132,38,0.85); }
  .theme {
    left: 0; top: 312px; width: 894px; text-align: center; white-space: nowrap;
    font: 700 56px/1 "Playfair Display", serif; color: var(--title-red); letter-spacing: 3px;
  }
  .theme .joiner { font: 400 84px/0 "Great Vibes", cursive; color: var(--ink-white); letter-spacing: 0; margin: 0 10px; }
  .focus-band { left: 0; top: 377px; width: 894px; height: 75px; background: linear-gradient(90deg, #d83a2f 0%, rgba(226,80,40,0.6) 70%, rgba(236,120,40,0) 100%); }
  .focus {
    left: 74px; top: 383px; width: 760px; display: flex; justify-content: space-between;
    font: 400 18px/1 "Libre Baskerville", serif; letter-spacing: 11px;
  }
  .section-band {
    left: 0; width: 470px; height: 71px;
    background: linear-gradient(90deg, var(--band-orange) 70%, rgba(238,132,38,0));
  }
  .section-band.date { top: 452px; }
  .section-band.venue { top: 788px; }
  .section-label { font: 400 66px/1 "Great Vibes", cursive; color: var(--title-red); }
  .section-label.date { left: 150px; top: 457px; }
  .section-label.venue { left: 136px; top: 792px; }
  .schedule-block {
    left: 0; top: 523px; width: 480px; height: 265px;
    background: linear-gradient(90deg, var(--deep-red) 60%, rgba(200,35,50,0));
  }
  .venue-block {
    left: 0; top: 859px; width: 480px; height: 130px;
    background: linear-gradient(90deg, #cf2e2f 55%, rgba(210,50,45,0));
  }
  .session { left: 100px; width: 360px; display: flex; align-items: center; }
  .session .day { width: 90px; text-align: right; font: 400 17px/1.3 "Open Sans", sans-serif; padding-right: 10px; border-right: 1.5px solid var(--ink-white); }
  .session .day strong { font-weight: 700; display: block; }
  .session .time { padding-left: 12px; font: 400 16px/1.55 "Libre Baskerville", serif; letter-spacing: 6px; }
  .session.s1 { top: 622px; top: 622px; }
  .session.s1 { top: 622px; }
  .venue-address {
    left: 20px; top: 944px; width: 420px; text-align: center;
    font: 400 14px/1.55 "Libre Baskerville", serif; letter-spacing: 5px; text-transform: uppercase;
  }
  .speaker-photo {
    left: 470px; top: 425px; width: 400px; height: 735px;
    background: radial-gradient(ellipse at 50% 40%, #d9582c 0%, #c8432a 45%, rgba(200,60,40,0.6) 75%, rgba(200,60,40,0) 100%);
  }
  .speaker-rule { top: 1018px; height: 1px; background: var(--speaker-orange); }
  .speaker-rule.left { left: 112px; width: 164px; }
  .speaker-rule.right { left: 659px; width: 124px; }
  .speaker-label { left: 356px; top: 970px; font: 400 52px/1 "Great Vibes", cursive; color: var(--speaker-orange); }
  .speaker-name {
    left: 100px; top: 1032px; width: 720px; text-align: center;
    font: 400 20px/1 "Libre Baskerville", serif; letter-spacing: 12px; text-transform: uppercase;
  }
  .brand { left: 24px; top: 1090px; display: flex; align-items: center; gap: 8px; }
  .brand-dot { width: 18px; height: 18px; border-radius: 50%; background: var(--speaker-orange); }
  .brand-name { font: 400 34px/1 "Playfair Display", serif; color: var(--ink-white); }
  .contact {
    left: 218px; top: 1104px; width: 676px; height: 42px; display: flex; align-items: center;
    background: linear-gradient(90deg, rgba(180,25,45,0.45), rgba(180,25,45,0));
    font: 400 15px/1 "Open Sans", sans-serif;
  }
  .contact .label { font: 400 28px/1 "Great Vibes", cursive; padding: 0 10px 0 6px; }
  .contact .item { padding: 0 10px; border-left: 1.5px solid var(--ink-white); white-space: nowrap; }
</style>
</head>
<body>
<main class="flyer">
  <div class="year">2020</div>
  <h1 class="event-name">KESTREL</h1>
  <div class="event-kind">Summit</div>
  <div class="title-rule left"></div>
  <div class="title-rule right"></div>

  <div class="theme-band"></div>
  <h2 class="theme">IN FIRE<span class="joiner">and</span>ON FIRE</h2>
  <div class="focus-band"></div>
  <p class="focus"><span>FIRE</span><span>•</span><span>REVIVAL</span><span>•</span><span>PROPHETIC</span></p>

  <div class="section-band date"></div>
  <h3 class="section-label date">Date</h3>
  <div class="schedule-block"></div>
  <div class="session" style="top:563px"><div class="day">THU<strong>DEC 31</strong></div><div class="time">OPENING<br>6:30PM</div></div>
  <div class="session" style="top:634px"><div class="day">FRI/SAT<strong>JAN 1&amp; 2</strong></div><div class="time">OPENING<br>6:30PM</div></div>
  <div class="session" style="top:710px"><div class="day">SUN<strong>JAN 3</strong></div><div class="time">OPENING<br>4:30PM</div></div>

  <div class="section-band venue"></div>
  <h3 class="section-label venue">Venue</h3>
  <div class="venue-block"></div>
  <p class="venue-address" style="top:874px">Harlow Community Center,<br>239 Fennimore Street,<br>Portland, ME 04117</p>

  <div class="speaker-photo" role="img" aria-label="Portrait of the speaker, Prophet Marcus Olunde, in an orange suit against flames"></div>

  <div class="speaker-rule left"></div>
  <div class="speaker-rule right"></div>
  <div class="speaker-label">Speaker</div>
  <p class="speaker-name">Prophet Marcus Olunde</p>

  <div class="brand"><span class="brand-dot"></span><span class="brand-name">HALCYON</span></div>

  <div class="contact">
    <span class="label">Contact Us</span>
    <span class="item">Email: contact@brightmeadowfold.org</span>
    <span class="item">phone: 207 583 2914</span>
  </div>
</main>
</body>
</html>
```